Baby prediction and advice cards, thank you notes, Baby shower invitations and diaper raffle tickets

Please see attached brief with description of the project.

*** Only apply if you are DETAIL ORIENTED and willing to read 100% the brief and the correction instructions (if required)***

*** Only apply if you are able to communicate in English 100%***

We need QUALITY over quantity

Contact us if you have questions.

Thank you

Target Market(s)

Expecting mothers and their families (Mothers, sisters)

Font styles to use
Sans Serif

Colors

Designer to choose colors to be used in the design.

Requirements
Must have
• Read the brief
Should not have
• Read the brief

```html
<!DOCTYPE html>
<html lang="en">
<head>
<meta charset="utf-8">
<title>Baby Shower Stationery Set</title>
<link rel="stylesheet" href="https://fonts.googleapis.com/css2?family=Amatic+SC:wght@400;700&display=swap">
<style>
  :root {
    --bg: #e9e9e9;
    --kraft: #cbb99b;
    --ink: #ffffff;
    --mint: #a8dccd;
    --cloud: rgba(255,255,255,0.28);
    --shadow: rgba(0,0,0,0.28);
  }
  * { box-sizing: border-box; margin: 0; padding: 0; }
  html, body { width: 1200px; height: 1000px; overflow: hidden; }
  body {
    background: var(--bg);
    font-family: "Amatic SC", "Arial Narrow", sans-serif;
    color: var(--ink);
    position: relative;
  }
  .card {
    position: absolute;
    background: var(--kraft);
    box-shadow: 3px 4px 8px var(--shadow);
  }
  .card-frame {
    position: absolute;
    inset: 10px;
    border: 1.5px dashed var(--ink);
    outline: 1.5px solid var(--mint);
    outline-offset: 3px;
  }
  .cloud {
    position: absolute;
    background: var(--cloud);
    border-radius: 50% 50% 40% 40%;
  }
  .title-rule {
    height: 2px;
    background: var(--mint);
    margin: 4px auto;
  }
  .field {
    position: absolute;
    display: flex;
    align-items: flex-end;
    gap: 6px;
    font-size: 19px;
    font-weight: 700;
    letter-spacing: 0.5px;
  }
  .field .line { flex: 1; border-bottom: 1.5px solid var(--ink); height: 1px; margin-bottom: 5px; }
  .moon { width: 14px; height: 14px; flex: none; margin-bottom: 5px; }
  .box { width: 22px; height: 20px; border: 1.5px solid var(--ink); display: inline-block; }

  /* Prediction card */
  .prediction { left: 55px; top: 55px; width: 590px; height: 420px; }
  .prediction-title { position: absolute; left: 0; right: 0; top: 28px; text-align: center; }
  .prediction-title .big { font-size: 46px; font-weight: 700; letter-spacing: 3px; line-height: 1; }
  .prediction-title .sub { font-size: 24px; font-weight: 700; }

  /* Message card */
  .message { left: 670px; top: 65px; width: 400px; height: 300px; }
  .message-text {
    position: absolute; left: 50px; right: 50px; top: 110px;
    text-align: center; font-size: 22px; font-weight: 700; letter-spacing: 1px; line-height: 1.15;
  }

  /* Raffle ticket */
  .raffle { left: 65px; top: 565px; width: 305px; height: 185px; }
  .raffle-title { position: absolute; left: 0; right: 0; top: 28px; text-align: center; font-size: 24px; font-weight: 700; letter-spacing: 1px; }
  .raffle-text { position: absolute; left: 30px; right: 30px; top: 72px; text-align: center; font-size: 18px; font-weight: 700; line-height: 1.1; }

  /* Invitation */
  .invite { left: 378px; top: 470px; width: 365px; height: 500px; }
  .invite-title { position: absolute; left: 0; right: 0; top: 120px; text-align: center; font-weight: 700; line-height: 0.95; }
  .invite-title .small { font-size: 27px; letter-spacing: 2px; }
  .invite-title .large { font-size: 52px; letter-spacing: 3px; }
  .invite-lede { position: absolute; left: 30px; right: 20px; top: 268px; text-align: center; font-size: 20px; font-weight: 700; }

  /* Folded thank-you card */
  .folded { left: 705px; top: 350px; width: 455px; height: 610px; }
  .folded .panel { position: absolute; left: 0; right: 0; height: 305px; }
  .folded .panel-top { top: 0; }
  .folded .panel-bottom { top: 305px; border-top: 1px solid rgba(0,0,0,0.08); }
  .thanks { position: absolute; left: 0; right: 0; top: 120px; text-align: center; font-size: 48px; font-weight: 700; letter-spacing: 3px; }
</style>
</head>
<body>
<svg width="0" height="0" style="position:absolute">
  <defs>
    <symbol id="moon" viewBox="0 0 14 14">
      <path d="M9 1.5A6 6 0 1 0 12.5 10 5 5 0 0 1 9 1.5Z" fill="none" stroke="#a8dccd" stroke-width="2"/>
    </symbol>
  </defs>
</svg>

<!-- Prediction and advice card -->
<section class="card prediction">
  <div class="card-frame"></div>
  <div class="cloud" role="img" aria-label="doodled cloud" style="left:45px;top:55px;width:44px;height:30px"></div>
  <div class="cloud" role="img" aria-label="doodled cloud" style="left:95px;top:55px;width:34px;height:24px"></div>
  <div class="cloud" role="img" aria-label="doodled cloud" style="left:450px;top:35px;width:34px;height:24px"></div>
  <div class="cloud" role="img" aria-label="doodled cloud" style="left:500px;top:30px;width:40px;height:28px"></div>
  <div class="cloud" role="img" aria-label="doodled cloud" style="left:255px;top:205px;width:40px;height:28px"></div>
  <div class="cloud" role="img" aria-label="doodled cloud" style="left:75px;top:290px;width:40px;height:28px"></div>
  <div class="prediction-title">
    <div class="big">Baby</div>
    <div class="title-rule" style="width:150px"></div>
    <div class="sub">prediction and advice</div>
  </div>
  <div class="field" style="left:50px;top:128px;width:250px"><svg class="moon"><use href="#moon"/></svg>Baby's name:<span class="line"></span></div>
  <div class="field" style="left:50px;top:165px;width:240px"><svg class="moon"><use href="#moon"/></svg>Gender: Boy <span class="box"></span>&nbsp; Weight:</div>
  <div class="field" style="left:122px;top:190px;width:180px">Girl <span class="box"></span>&nbsp;&nbsp; Length:</div>
  <div class="field" style="left:50px;top:260px;width:230px"><svg class="moon"><use href="#moon"/></svg>Resemblance: All dad <span class="box"></span></div>
  <div class="field" style="left:145px;top:282px;width:110px">All mom <span class="box"></span></div>
  <div class="field" style="left:145px;top:304px;width:110px">Both &nbsp;&nbsp;&nbsp; <span class="box"></span></div>
  <div class="field" style="left:50px;top:340px;width:230px"><svg class="moon"><use href="#moon"/></svg>My best advice:<span class="line"></span></div>
  <div class="field" style="left:60px;top:370px;width:220px"><span class="line"></span></div>
  <div class="field" style="left:320px;top:108px;width:225px"><svg class="moon"><use href="#moon"/></svg>Date of birth:<span class="line"></span></div>
  <div class="field" style="left:320px;top:138px;width:225px"><svg class="moon"><use href="#moon"/></svg>Time of birth:<span class="line"></span></div>
  <div class="field" style="left:320px;top:170px;width:225px"><svg class="moon"><use href="#moon"/></svg>Hair color:<span class="line"></span></div>
  <div class="field" style="left:320px;top:198px;width:225px"><svg class="moon"><use href="#moon"/></svg>Eye color:<span class="line"></span></div>
  <div class="field" style="left:275px;top:245px;width:280px"><svg class="moon"><use href="#moon"/></svg>I hope you get dad's:<span class="line"></span></div>
  <div class="field" style="left:275px;top:280px;width:280px"><svg class="moon"><use href="#moon"/></svg>I hope you get mom's:<span class="line"></span></div>
  <div class="field" style="left:275px;top:320px;width:280px"><svg class="moon"><use href="#moon"/></svg>Best wishes and love from:<span class="line"></span></div>
  <div class="field" style="left:295px;top:352px;width:260px"><span class="line"></span></div>
</section>

<!-- Thank-you message card -->
<section class="card message">
  <div class="cloud" role="img" aria-label="doodled cloud" style="left:30px;top:70px;width:40px;height:28px"></div>
  <div class="cloud" role="img" aria-label="doodled cloud" style="left:82px;top:68px;width:34px;height:24px"></div>
  <div class="cloud" role="img" aria-label="doodled cloud" style="left:35px;top:120px;width:28px;height:20px"></div>
  <div class="cloud" role="img" aria-label="doodled cloud" style="left:345px;top:235px;width:34px;height:24px"></div>
  <div class="title-rule" style="position:absolute;left:145px;top:100px;width:110px"></div>
  <p class="message-text">"For being with me and sharing in the celebration of this wonderful occasion."</p>
</section>

<!-- Diaper raffle ticket -->
<section class="card raffle">
  <div class="card-frame"></div>
  <div class="raffle-title">Diaper raffle ticket</div>
  <div class="title-rule" style="position:absolute;left:70px;top:62px;width:165px"></div>
  <p class="raffle-text">Bring a pack of diapers (any size) for your chance to win a prize!</p>
  <div class="field" style="left:55px;top:132px;width:210px">Name:<span class="line"></span></div>
</section>

<!-- Invitation -->
<section class="card invite">
  <div class="card-frame"></div>
  <div class="cloud" role="img" aria-label="doodled cloud" style="left:40px;top:30px;width:44px;height:30px"></div>
  <div class="cloud" role="img" aria-label="doodled cloud" style="left:95px;top:42px;width:30px;height:22px"></div>
  <div class="cloud" role="img" aria-label="doodled cloud" style="left:40px;top:70px;width:30px;height:22px"></div>
  <div class="cloud" role="img" aria-label="doodled cloud" style="left:215px;top:440px;width:30px;height:22px"></div>
  <div class="cloud" role="img" aria-label="doodled cloud" style="left:258px;top:425px;width:44px;height:30px"></div>
  <div class="invite-title">
    <div class="small">Celebrating</div>
    <div class="large">A Baby</div>
    <div class="small">on the way</div>
  </div>
  <p class="invite-lede">"Join us for a shower honoring:</p>
  <div class="field" style="left:45px;top:300px;width:230px"><svg class="moon"><use href="#moon"/></svg>Time:<span class="line"></span></div>
  <div class="field" style="left:45px;top:330px;width:230px"><svg class="moon"><use href="#moon"/></svg>Place:<span class="line"></span></div>
  <div class="field" style="left:45px;top:360px;width:230px"><svg class="moon"><use href="#moon"/></svg>Details:<span class="line"></span></div>
  <div class="field" style="left:105px;top:390px;width:170px"><span class="line"></span></div>
  <div class="field" style="left:45px;top:418px;width:230px"><svg class="moon"><use href="#moon"/></svg>RSVP to:<span class="line"></span></div>
  <div class="field" style="left:45px;top:446px;width:230px"><svg class="moon"><use href="#moon"/></svg>Hosted by:<span class="line"></span></div>
</section>

<!-- Folded thank-you card -->
<section class="card folded">
  <div class="panel panel-top">
    <div class="card-frame"></div>
    <div class="cloud" role="img" aria-label="doodled cloud" style="left:190px;top:90px;width:34px;height:24px"></div>
  </div>
  <div class="panel panel-bottom">
    <div class="card-frame"></div>
    <div class="cloud" role="img" aria-label="doodled cloud" style="left:45px;top:25px;width:44px;height:30px"></div>
    <div class="cloud" role="img" aria-label="doodled cloud" style="left:100px;top:45px;width:30px;height:22px"></div>
    <div class="cloud" role="img" aria-label="doodled cloud" style="left:55px;top:65px;width:30px;height:22px"></div>
    <div class="cloud" role="img" aria-label="doodled cloud" style="left:330px;top:245px;width:30px;height:22px"></div>
    <div class="cloud" role="img" aria-label="doodled cloud" style="left:372px;top:232px;width:44px;height:30px"></div>
    <div class="thanks">"Thank you"</div>
  </div>
</section>
</body>
</html>
```